MOLVT Study flyer

I need help designing a flyer for a research study that will include brain imaging in adolescents. The info is in the attached document. The study is called the Marrowby Orchard Lantern Vesper Trail (MOLVT) study. Ideally this would be returned as a document that I can edit in the future as we will have several new recruitment phases (different age groups, etc. I also would love to have a logo designed as part of this project, but I recognize that might be a separate design request.

```html
<!DOCTYPE html>
<html lang="en">
<head>
<meta charset="utf-8">
<title>MOLVT Study Flyer</title>
<link rel="stylesheet" href="https://fonts.googleapis.com/css2?family=Oswald:wght@600&family=Raleway:wght@400;500;800&display=swap">
<style>
  :root {
    --navy: #1f3556;
    --navy-deep: #172a47;
    --orange: #e8990c;
    --white: #ffffff;
    --ink: #2b3a52;
    --stage: #d9dde2;
    --rule: #e9d9b8;
  }
  * { box-sizing: border-box; margin: 0; padding: 0; }
  html, body { width: 1200px; height: 2400px; overflow: hidden; }
  body { background: var(--stage); font-family: "Raleway", sans-serif; color: var(--ink); }

  .flyer {
    position: absolute; left: 40px; top: 411px;
    width: 1120px; height: 1577px;
    background: var(--white); overflow: hidden;
    box-shadow: 0 10px 30px rgba(0,0,0,.18);
  }
  .hero-art { position: absolute; left: 0; top: 0; width: 1120px; height: 760px; }

  .study-name {
    position: absolute; top: 62px; width: 100%; text-align: center;
    font-weight: 500; font-size: 92px;
    color: var(--orange); letter-spacing: 2px; line-height: 1;
  }
  .kicker {
    position: absolute; top: 182px; width: 100%; text-align: center;
    font-family: "Oswald", sans-serif; font-weight: 600; font-size: 38px;
    color: var(--white); line-height: 1;
  }
  .headline {
    position: absolute; top: 240px; width: 100%; text-align: center;
    font-weight: 800; font-size: 54px; line-height: 66px; color: var(--white);
  }

  .intro {
    position: absolute; top: 800px; left: 60px; width: 1000px; text-align: center;
    font-size: 22px; line-height: 28px; color: var(--ink);
  }

  .participation {
    position: absolute; left: 88px; top: 900px; width: 499px; height: 446px;
    background: var(--orange); border-radius: 46px; padding: 52px 36px 0 36px; color: var(--white);
  }
  .participation h2 { font-weight: 800; font-size: 36px; line-height: 42px; margin-bottom: 24px; }
  .participation ul { list-style: none; }
  .participation li {
    position: relative; padding-left: 32px; font-size: 18px; line-height: 22px; margin-bottom: 22px;
  }
  .participation li svg { position: absolute; left: 0; top: 2px; width: 22px; height: 22px; }

  .eligibility { position: absolute; left: 650px; top: 945px; width: 420px; }
  .eligibility h2 { font-weight: 800; font-size: 36px; line-height: 43px; color: var(--navy); margin-bottom: 14px; }
  .criteria { list-style: none; }
  .criterion {
    position: relative; padding: 30px 0 16px 82px;
    font-size: 21px; line-height: 26px; color: var(--ink);
  }
  .criterion:first-child { padding-top: 0; }
  .criterion + .criterion::before {
    content: ""; position: absolute; left: 0; top: 0;
    width: 332px; height: 2px; background: var(--rule);
  }
  .criterion svg { position: absolute; left: 20px; top: 22px; width: 46px; height: 46px; }
  .criterion:first-child svg { top: -10px; }
  .criterion .label { display: block; width: 300px; }

  .contact-prompt {
    position: absolute; left: 101px; top: 1372px; z-index: 1;
    font-weight: 800; font-size: 27px; line-height: 34px; color: var(--navy);
  }
  .email {
    position: absolute; left: 97px; top: 1455px; height: 64px; padding: 0 22px; z-index: 1;
    background: var(--orange); border-radius: 32px;
    font-weight: 500; font-size: 42px; line-height: 62px; color: var(--white);
  }
  .footer-band { position: absolute; left: 0; bottom: 0; width: 1120px; height: 90px; }
  .brain-art { position: absolute; left: 790px; top: 1291px; width: 300px; height: 286px; }
</style>
</head>
<body>
<main class="flyer">
  <svg class="hero-art" viewBox="0 0 1120 760">
    <defs>
      <linearGradient id="photoTone" x1="0" y1="0" x2="1" y2="1">
        <stop offset="0" stop-color="#e9e1cf"/>
        <stop offset=".5" stop-color="#e6b6a6"/>
        <stop offset="1" stop-color="#e6c15a"/>
      </linearGradient>
      <linearGradient id="navyFade" x1="0" y1="0" x2="0" y2="1">
        <stop offset="0" stop-color="#2a4163"/>
        <stop offset="1" stop-color="#1f3556"/>
      </linearGradient>
    </defs>
    <rect role="img" aria-label="Photo of a doctor giving a high five to a smiling girl while her mother looks on" x="0" y="0" width="1120" height="760" fill="url(#photoTone)"/>
    <path d="M0 0 H1120 V346 Q900 300 800 420 Q560 520 320 420 Q200 300 0 346 Z" fill="url(#navyFade)"/>
    <path d="M0 629 Q300 790 560 755 Q860 715 1120 645 V760 H0 Z" fill="#ffffff"/>
  </svg>

  <div class="study-name">MOLVT</div>
  <div class="kicker">ARE YOU THE PARENT OF A CHILD AGE 10-17?</div>
  <h1 class="headline">DO THEY WORRY OR OVERTHINK<br>NEGATIVE EMOTIONS?</h1>

  <p class="intro">Harlow Ridge University researchers are seeking girls age 10-17 for a study about brain activity in emotions and decision-making and how they relate to puberty, anxiety and depression.</p>

  <section class="participation">
    <h2>STUDY PARTICIPATION<br>INVOLVES</h2>
    <ul>
      <li><svg viewBox="0 0 22 22"><circle cx="11" cy="11" r="9" fill="none" stroke="#1f3556" stroke-width="2"/><path d="M6.5 11.5l3 3 6-6" fill="none" stroke="#1f3556" stroke-width="2"/></svg>One one-hour interview (online or in-person) where your child will discuss their thoughts</li>
      <li><svg viewBox="0 0 22 22"><circle cx="11" cy="11" r="9" fill="none" stroke="#1f3556" stroke-width="2"/><path d="M6.5 11.5l3 3 6-6" fill="none" stroke="#1f3556" stroke-width="2"/></svg>Online questionnaires (parent and child)</li>
      <li><svg viewBox="0 0 22 22"><circle cx="11" cy="11" r="9" fill="none" stroke="#1f3556" stroke-width="2"/><path d="M6.5 11.5l3 3 6-6" fill="none" stroke="#1f3556" stroke-width="2"/></svg>One two-hour visit where your child will complete an MRI scan, answer questions</li>
      <li><svg viewBox="0 0 22 22"><circle cx="11" cy="11" r="9" fill="none" stroke="#1f3556" stroke-width="2"/><path d="M6.5 11.5l3 3 6-6" fill="none" stroke="#1f3556" stroke-width="2"/></svg>about their puberty stage, and have a small hair sample taken to study puberty hormones</li>
    </ul>
  </section>

  <section class="eligibility">
    <h2>YOUR CHILD MAY BE<br>ELIGIBLE IF THEY</h2>
    <ul class="criteria">
      <li class="criterion">
        <svg viewBox="0 0 50 50" fill="#e8990c"><circle cx="12" cy="22" r="4"/><rect x="7" y="27" width="10" height="16" rx="3"/><circle cx="25" cy="17" r="5"/><rect x="19" y="23" width="12" height="20" rx="3"/><circle cx="39" cy="12" r="5"/><rect x="33" y="18" width="12" height="25" rx="3"/></svg>
        <span class="label">Are age 10-17</span>
      </li>
      <li class="criterion">
        <svg viewBox="0 0 50 50" fill="#e8990c"><path d="M6 38 Q4 18 20 14 Q32 13 32 26 L28 30 V40 H14 V36 Z"/><circle cx="36" cy="12" r="7"/><circle cx="40" cy="32" r="7"/><rect x="36" y="31" width="8" height="2" fill="#fff"/><path d="M32.5 12h7M36 8.5v7" stroke="#fff" stroke-width="2"/></svg>
        <span class="label">Tend to worry or overthink negative thoughts</span>
      </li>
      <li class="criterion">
        <svg viewBox="0 0 50 50" fill="#e8990c"><rect x="6" y="4" width="28" height="38" rx="3"/><rect x="11" y="12" width="14" height="3" fill="#fff"/><rect x="11" y="20" width="10" height="3" fill="#fff"/><circle cx="32" cy="30" r="9" fill="#fff" stroke="#e8990c" stroke-width="4"/><path d="M38 37l8 8" stroke="#e8990c" stroke-width="5"/></svg>
        <span class="label">have not been diagnosed with psychosis, learning problems, or autism</span>
      </li>
    </ul>
  </section>

  <svg class="footer-band" viewBox="0 0 1120 90" preserveAspectRatio="none"><path d="M0 45 Q500 20 1120 40 V90 H0 Z" fill="#172a47"/></svg>
  <svg class="brain-art" viewBox="0 0 300 286" role="img" aria-label="Photo of cupped hands holding a brain made of white puzzle pieces">
    <defs><radialGradient id="brainTone" cx=".55" cy=".6" r=".5"><stop offset="0" stop-color="#f2efec"/><stop offset=".7" stop-color="#e3c4b3"/><stop offset="1" stop-color="#e3c4b3" stop-opacity="0"/></radialGradient></defs>
    <rect width="300" height="286" fill="url(#brainTone)"/>
  </svg>

  <p class="contact-prompt">INTERESTED IN PARTICIPATING?<br>WANT MORE INFORMATION? PLEASE CONTACT US!</p>
  <div class="email">molvtstudy@harlowridge.edu</div>
</main>
</body>
</html>
```